Hot sauce company needs a logo and label design- simple, clean & fresh

Wendel T's a hot pepper sauce company based on the edge of London needs a logo and label design .
The sauces are handmade in small batches with natural ingredients , no added sugars or extracts and so we would like a clean fresh label to reflect this - avoiding all the macho devil and flames novelty stuff.
At present there are four sauces - Jalapeno ,Chipotle,Habanero and Reaper we would like to have one Wendel T's label with the name of the sauce being changeable allowing us to react to what ingredients are available .
Updates

Project Deadline Extended
Reason: Hi Guys I have received a few requests to extend the deadline on the project and so I am thanks Wendel T's

Target Market(s)

people who care what they eat

Industry/Entity Type

Food Store

Logo Text

Wendel T's handmade hot sauce

Requirements
Must have
• Wendel T's handmade hot sauce - or the logo
• the name of the sauce ie jalapeno
• no added sugars
Nice to have
• handmade
• small batch
Should not have
• cartoon men with smoke coming out of their ears
• devils and the flames of hell

```html
<!DOCTYPE html>
<html lang="en">
<head>
<meta charset="utf-8">
<title>Wendel T's — Hot Sauce Labels</title>
<link rel="stylesheet" href="https://fonts.googleapis.com/css2?family=Fredoka:wght@700&family=Open+Sans:wght@400;800&display=swap">
<style>
  :root {
    --page: #ffffff;
    --paper: #f0eee9;
    --brand-brown: #7a5a55;
    --text-light: #ffffff;
    --jalapeno: #00a538;
    --habanero: #e8973a;
    --reaper: #b81a36;
    --chipotle: #7c2a30;
  }
  * { box-sizing: border-box; margin: 0; padding: 0; }
  html, body {
    width: 1200px;
    height: 1138px;
    overflow: hidden;
    background: var(--page);
    font-family: "Open Sans", Arial, sans-serif;
  }
  .label-sheet {
    position: relative;
    width: 1200px;
    height: 1138px;
  }
  .label {
    position: absolute;
    width: 485px;
    height: 485px;
    background: var(--paper);
  }
  .label--jalapeno { left: 102px; top: 72px;  --accent: var(--jalapeno); }
  .label--habanero { left: 614px; top: 72px;  --accent: var(--habanero); }
  .label--reaper   { left: 102px; top: 582px; --accent: var(--reaper); }
  .label--chipotle { left: 614px; top: 582px; --accent: var(--chipotle); }

  .label__frame {
    position: absolute;
    left: 16px;
    right: 13px;
    top: 12px;
    bottom: 13px;
    border: 2px solid var(--accent);
  }
  .label__brand {
    position: absolute;
    left: 0;
    right: 0;
    top: 50px;
    text-align: center;
    font-weight: 800;
    font-size: 36px;
    line-height: 1;
    letter-spacing: 1px;
    color: var(--brand-brown);
  }
  .label__tagline {
    position: absolute;
    left: 0;
    right: 0;
    top: 98px;
    text-align: center;
    font-weight: 800;
    font-size: 13px;
    line-height: 1;
    letter-spacing: 2px;
    text-transform: uppercase;
    color: var(--brand-brown);
  }
  .label__art {
    position: absolute;
    left: 66px;
    top: 150px;
    width: 352px;
    height: 215px;
    background: var(--accent);
    border-radius: 50% / 45%;
  }
  .label__sauce {
    position: absolute;
    left: 66px;
    top: 150px;
    width: 352px;
    height: 215px;
    display: flex;
    flex-direction: column;
    align-items: center;
    justify-content: center;
    font-family: "Fredoka", "Arial Rounded MT Bold", sans-serif;
    font-weight: 700;
    font-size: 58px;
    line-height: 0.95;
    text-transform: uppercase;
    color: var(--text-light);
    text-align: center;
  }
  .label__sauce--stacked { font-size: 62px; }
  .label__band {
    position: absolute;
    left: 16px;
    right: 13px;
    top: 409px;
    bottom: 13px;
    background: var(--accent);
  }
  .label__claims {
    position: absolute;
    left: 155px;
    width: 176px;
    top: 388px;
    height: 60px;
    padding-top: 12px;
    background: var(--accent);
    border-radius: 10px 10px 0 0;
    color: var(--text-light);
    font-size: 12px;
    line-height: 15px;
    text-align: center;
    list-style: none;
  }
</style>
</head>
<body>
<main class="label-sheet">

  <section class="label label--jalapeno">
    <div class="label__frame"></div>
    <p class="label__brand">Wendel T's</p>
    <p class="label__tagline">handmade hot sauce</p>
    <div class="label__art" role="img" aria-label="Green jalapeño pepper illustration with splashes"></div>
    <h2 class="label__sauce">Jalapeño</h2>
    <div class="label__band"></div>
    <ul class="label__claims">
      <li>natural ingredients</li>
      <li>no added sugars</li>
      <li>small batch</li>
    </ul>
  </section>

  <section class="label label--habanero">
    <div class="label__frame"></div>
    <p class="label__brand">Wendel T's</p>
    <p class="label__tagline">handmade hot sauce</p>
    <div class="label__art" role="img" aria-label="Orange habanero pepper illustration with splashes"></div>
    <h2 class="label__sauce label__sauce--stacked"><span>Haba</span><span>nero</span></h2>
    <div class="label__band"></div>
    <ul class="label__claims">
      <li>natural ingredients</li>
      <li>no added sugars</li>
      <li>small batch</li>
    </ul>
  </section>

  <section class="label label--reaper">
    <div class="label__frame"></div>
    <p class="label__brand">Wendel T's</p>
    <p class="label__tagline">handmade hot sauce</p>
    <div class="label__art" role="img" aria-label="Red reaper pepper illustration with splashes"></div>
    <h2 class="label__sauce label__sauce--stacked"><span>Rea</span><span>per</span></h2>
    <div class="label__band"></div>
    <ul class="label__claims">
      <li>natural ingredients</li>
      <li>no added sugars</li>
      <li>small batch</li>
    </ul>
  </section>

  <section class="label label--chipotle">
    <div class="label__frame"></div>
    <p class="label__brand">Wendel T's</p>
    <p class="label__tagline">handmade hot sauce</p>
    <div class="label__art" role="img" aria-label="Dark red chipotle pepper illustration with splashes"></div>
    <h2 class="label__sauce">Chipotle</h2>
    <div class="label__band"></div>
    <ul class="label__claims">
      <li>natural ingredients</li>
      <li>no added sugars</li>
      <li>small batch</li>
    </ul>
  </section>

</main>
</body>
</html>
```